Basic Commercial & Residential Real Estate Web Site

I need a basic website for a new real estate company that deals with both residential and commercial sales. It must be clean and professional. We sell homes, office buildings, farms, and ranches. It should feel crisp and clean.
I need a main page with my logo and links to commercial, residential, farm and land searches with contact data forms. Also incorporated would be a mls property search (IDX) form. I am in Northern California and the current site I posted is at www.qlvantor.com. I need the functionality of the links and the supporting pages. I do not have all the copy ready because I did not know what to expect.
Updates

Project Deadline Extended
Reason: I apologize, I am extremely busy and you all need more data to do a good job. All the designs are great so far and it is extremely difficult to choose at this point. I haven't given you enough data. I haver now uploaded some relevent photos (not very good) and edited the brief. I am looking for what I call the Landing or main page with some functionality built in to other pages which I also need. Example if you click on "Commercial" it should go to a page that discusses our commercial dept.......

I would like to thank all the designers for all their hard work and efforts, I wish I could reward you all.

Thanks again for your creative and professional designs.

Frank

Target Market(s)

Corporate Execs for the Commercial Buildings
Homeowners/Families for the Homes and Farms
Upper end people for the land to build estates

Industry/Entity Type

Real Estate

Font styles to use
Sans Serif

Requirements
Must have
• Our Logo should be prominent, pronounced
Need contact data or button
Functional Page that links to other data pages
Must Have a "search for properties" feature
Must say "Commercial and Residential Representation"
Pictures of Commercial Building and Nice Home (Tradtional not contemporary)
Nice to have
• Individual Buttons or links to "Commercial, Residential, Farm/Ranch, Land"
Contact Data displayed
button that says "Maple Crest"-next to button is Maple Crest Logo-see www.maplecrest.bz
Links to "Buyers and "Sellers"
Links to Facebook, twitter,.....etc
Should not have
• 20+ story commercial buildings or ultra modern. See uploaded files of typical buildings for commercial.

```html
<!DOCTYPE html>
<html lang="en">
<head>
<meta charset="utf-8">
<title>Qlvantor Properties</title>
<link href="https://fonts.googleapis.com/css2?family=Open+Sans:wght@400;600;700&display=swap" rel="stylesheet">
<style>
:root{
  --blue:#1b95dc;
  --blue-dark:#137bb8;
  --orange:#f2891d;
  --navy:#1d2939;
  --navy-deep:#141d29;
  --ink:#3a3f45;
  --muted:#8a9099;
  --line:#e2e5e9;
  --page:#ffffff;
  --soft:#f4f6f8;
}
*{box-sizing:border-box;margin:0;padding:0}
html,body{width:820px;height:1200px;overflow:hidden}
body{font-family:"Open Sans",Arial,sans-serif;color:var(--ink);background:var(--page);font-size:7px;line-height:1.45}
.canvas{position:relative;width:820px;height:1200px;overflow:hidden}

/* header + hero */
.hero{position:relative;height:340px;background:linear-gradient(180deg,#6f9fc8 0%,#a9c7df 38%,#d7dfe4 60%,#6f8a62 82%,#45603d 100%)}
.hero-photo{position:absolute;inset:0}
.hero-house{position:absolute;left:310px;top:70px;width:380px;height:230px;background:linear-gradient(180deg,#f3f3f1,#d9dcdc);opacity:.85}
.site-header{position:absolute;top:0;left:0;right:0;height:52px;background:linear-gradient(180deg,rgba(15,25,38,.75),rgba(15,25,38,0));display:flex;align-items:flex-start;justify-content:space-between;padding:0 120px 0 132px}
.brand{display:flex;align-items:center;gap:6px;margin-top:12px;color:#fff;font-weight:700;font-size:20px;letter-spacing:1px}
.brand-mark{width:10px;height:10px;background:#fff}
.main-nav{display:flex}
.main-nav a{display:block;color:#fff;text-decoration:none;font-size:7px;padding:8px 13px 10px;font-weight:600}
.main-nav a.active{background:var(--blue);padding-top:14px;padding-bottom:16px}
.slide-arrow{position:absolute;top:170px;width:18px;height:26px;background:rgba(20,30,45,.6);display:flex;align-items:center;justify-content:center}
.slide-arrow.left{left:0}.slide-arrow.right{right:0}

.search-panel{position:absolute;left:135px;top:95px;width:165px;background:var(--blue);padding:10px 10px 12px;color:#fff}
.search-panel label{display:block;font-size:6.5px;font-weight:600;margin:4px 0 2px}
.field{height:14px;background:#fff;border-radius:2px;color:var(--muted);font-size:6px;padding:3px 5px;display:flex;justify-content:space-between}
.field-row{display:flex;gap:6px}.field-row>div{flex:1}
.checks{display:flex;gap:18px;margin:8px 0 4px}
.check{display:flex;align-items:center;gap:4px;font-size:6px}
.check i{width:7px;height:7px;background:#fff;display:block}
.filter-btn{margin:10px auto 0;width:70px;height:18px;background:var(--navy);color:#fff;font-weight:700;font-size:7px;text-align:center;line-height:18px;border-radius:2px}

/* layout */
.container{position:absolute;left:130px;width:570px}
.col-main{position:absolute;left:0;width:345px}
.col-side{position:absolute;left:362px;width:208px}
h2{font-size:12px;font-weight:600;color:var(--ink)}
h2 span{color:var(--blue)}

.welcome{top:352px;height:120px}
.welcome p{margin-top:6px;font-size:6px;color:var(--muted);line-height:1.6}
.read-more{display:inline-block;margin-top:5px;color:var(--blue);font-size:6px;font-weight:600}
.welcome-photo{position:absolute;top:0;height:102px;background:linear-gradient(135deg,#cfd6dc,#8a98a4 60%,#5d6b78)}

.properties{top:488px}
.tabs{display:flex;margin-top:8px;border-bottom:2px solid var(--blue)}
.tabs span{padding:4px 14px;font-size:7px;font-weight:600;background:var(--soft);color:var(--ink)}
.tabs span.on{background:var(--blue);color:#fff}
.cards{display:grid;grid-template-columns:repeat(4,1fr);gap:10px;margin-top:10px}
.card{height:140px}
.card-photo{height:56px;background:linear-gradient(180deg,#8fb7d9,#c9d3d8 55%,#6d8a5c)}
.card-photo.b{background:linear-gradient(180deg,#7fb0de,#e0e2de 55%,#5f8d9f)}
.card-title{font-size:6px;font-weight:600;margin-top:4px;display:flex;justify-content:space-between;align-items:center}
.price{background:var(--orange);color:#fff;font-size:5.5px;padding:1px 3px}
.specs{display:flex;justify-content:space-between;font-size:5.5px;color:var(--muted);margin-top:5px;border-top:1px solid var(--line);padding-top:3px}
.more-btn{position:absolute;right:0;top:362px;background:var(--orange);color:#fff;font-size:7px;font-weight:600;padding:4px 12px}

.agent{display:flex;gap:8px;margin-top:12px;align-items:center}
.agent-photo{width:36px;height:36px;border-radius:50%;background:linear-gradient(180deg,#c8cdd2,#8d959d)}
.agent b{display:block;font-size:7px}
.agent small{display:block;font-size:5.5px;color:var(--muted)}
.featured{margin-top:16px;border:1px solid var(--line);padding:8px}
.featured-photo{height:88px;background:linear-gradient(180deg,#7aa9d4,#d3d6d2 55%,#6f8c5a)}
.featured h3{color:var(--blue);font-size:7.5px;margin-top:6px;font-weight:700}
.featured p{font-size:6px;color:var(--muted);margin-top:3px}
.detail-btn{display:block;margin:6px auto 0;width:72px;text-align:center;background:var(--orange);color:#fff;font-size:6.5px;font-weight:600;padding:3px 0}

.partners{top:886px;text-align:center}
.partner-row{display:flex;justify-content:space-between;margin-top:16px}
.partner-row i{display:block;width:52px;height:18px;background:#cfd4da;border-radius:2px}

.contact-strip{top:996px;display:flex;justify-content:space-between;font-size:6px;color:var(--muted)}
.contact-strip div{display:flex;align-items:center;gap:4px}

.footer{position:absolute;left:0;right:0;top:1018px;height:154px;background:var(--navy);color:#b9c1cb}
.footer .container{top:14px;display:grid;grid-template-columns:1.2fr 1fr .8fr 1.1fr;gap:22px}
.footer .brand{margin:0;font-size:16px}
.footer h4{color:#fff;font-size:8px;font-weight:600;margin-bottom:8px}
.footer p,.footer li{font-size:6px;line-height:1.7}
.footer ul{list-style:none}
.footer li{display:flex;align-items:center;gap:4px}
.news-input{margin-top:8px;display:flex}
.news-input span{flex:1;height:14px;background:#2c3a4d}
.news-input b{width:20px;height:14px;background:var(--blue)}
.copyright{position:absolute;left:0;right:0;top:1172px;height:28px;background:var(--navy-deep);color:#8c96a3;font-size:6px}
.copyright .container{top:9px;display:flex;justify-content:space-between}
.socials{display:flex;gap:5px}
.socials i{width:10px;height:10px;border-radius:50%;background:#3a4a5f;display:block}
</style>
</head>
<body>
<div class="canvas">

  <section class="hero">
    <div class="hero-photo" role="img" aria-label="Photo of a white two-storey traditional home behind palm trees under a blue sky"></div>
    <div class="hero-house" role="img" aria-label="Traditional family home facade"></div>
    <header class="site-header">
      <div class="brand"><span class="brand-mark"></span>QLVANTOR</div>
      <nav class="main-nav">
        <a class="active" href="#">Home</a>
        <a href="#">Commercial</a>
        <a href="#">Residential</a>
        <a href="#">Farm</a>
        <a href="#">Acquirement</a>
        <a href="#">Contact</a>
      </nav>
    </header>
    <div class="slide-arrow left"><svg width="6" height="10" viewBox="0 0 6 10"><path d="M5 1L1 5l4 4" stroke="#fff" stroke-width="1.5" fill="none"/></svg></div>
    <div class="slide-arrow right"><svg width="6" height="10" viewBox="0 0 6 10"><path d="M1 1l4 4-4 4" stroke="#fff" stroke-width="1.5" fill="none"/></svg></div>

    <form class="search-panel">
      <label>Location</label>
      <div class="field">Northern California <span>▾</span></div>
      <label>Type</label>
      <div class="field">Apartment <span>▾</span></div>
      <div class="field-row">
        <div><label>Beds</label><div class="field">1 <span>▾</span></div></div>
        <div><label>Baths</label><div class="field">1 <span>▾</span></div></div>
      </div>
      <div class="checks">
        <span class="check"><i></i>Rent</span>
        <span class="check"><i></i>Sale</span>
      </div>
      <div class="field-row">
        <div><label>Min Price</label><div class="field">$0 <span>▾</span></div></div>
        <div><label>Max Price</label><div class="field">$900k <span>▾</span></div></div>
      </div>
      <div class="filter-btn">Filter now!</div>
    </form>
  </section>

  <div class="container welcome" style="top:352px">
    <div class="col-main">
      <h2>Welcome To <span>Our Website</span></h2>
      <p>We help families, investors and business owners across Northern California find the right place to live, work and grow. Our team handles homes, office buildings, farms, ranches and open land with the same careful attention to detail.</p>
      <p>From your first search to the final signature, we guide buyers and sellers through every step, with clear advice, honest pricing and local knowledge built over many years in the region.</p>
      <a class="read-more">Read More »</a>
    </div>
    <div class="col-side welcome-photo" style="width:165px" role="img" aria-label="Bright living room interior with large windows"></div>
  </div>

  <div class="container properties">
    <div class="col-main">
      <h2>Properties</h2>
      <div class="tabs"><span class="on">Residential</span><span>Commercial</span></div>
      <div class="cards">
        <div class="card"><div class="card-photo" role="img" aria-label="Family home with lawn"></div><div class="card-title">Home in Redding<span class="price">$420k</span></div><div class="specs"><span>Garage</span><span>Baths</span><span>Beds</span></div><div class="specs"><span>2</span><span>2</span><span>3</span></div></div>
        <div class="card"><div class="card-photo b" role="img" aria-label="Suburban house exterior"></div><div class="card-title">Oak Lane House<span class="price">$385k</span></div><div class="specs"><span>Garage</span><span>Baths</span><span>Beds</span></div><div class="specs"><span>1</span><span>2</span><span>3</span></div></div>
        <div class="card"><div class="card-photo" role="img" aria-label="Ranch house with trees"></div><div class="card-title">Ranch in Chico<span class="price">$610k</span></div><div class="specs"><span>Garage</span><span>Baths</span><span>Beds</span></div><div class="specs"><span>2</span><span>3</span><span>4</span></div></div>
        <div class="card"><div class="card-photo b" role="img" aria-label="Home with swimming pool"></div><div class="card-title">Pool Villa<span class="price">$540k</span></div><div class="specs"><span>Garage</span><span>Baths</span><span>Beds</span></div><div class="specs"><span>2</span><span>2</span><span>4</span></div></div>
        <div class="card"><div class="card-photo b" role="img" aria-label="Home with garden"></div><div class="card-title">Garden Home<span class="price">$350k</span></div><div class="specs"><span>Garage</span><span>Baths</span><span>Beds</span></div><div class="specs"><span>1</span><span>1</span><span>2</span></div></div>
        <div class="card"><div class="card-photo" role="img" aria-label="Two-storey house"></div><div class="card-title">Hillside House<span class="price">$470k</span></div><div class="specs"><span>Garage</span><span>Baths</span><span>Beds</span></div><div class="specs"><span>2</span><span>2</span><span>3</span></div></div>
        <div class="card"><div class="card-photo b" role="img" aria-label="House with pool deck"></div><div class="card-title">Lake Retreat<span class="price">$695k</span></div><div class="specs"><span>Garage</span><span>Baths</span><span>Beds</span></div><div class="specs"><span>3</span><span>3</span><span>5</span></div></div>
        <div class="card"><div class="card-photo" role="img" aria-label="Country home"></div><div class="card-title">Farm House<span class="price">$520k</span></div><div class="specs"><span>Garage</span><span>Baths</span><span>Beds</span></div><div class="specs"><span>2</span><span>2</span><span>4</span></div></div>
      </div>
      <span class="more-btn">More</span>
    </div>

    <aside class="col-side">
      <h2>Our Agents</h2>
      <div class="agent"><div class="agent-photo" role="img" aria-label="Agent portrait"></div><div><b>Daniel Reyes</b><small>info@qlvantor.com</small><small>+1 530 555 0142</small></div></div>
      <div class="agent"><div class="agent-photo" role="img" aria-label="Agent portrait"></div><div><b>Laura Whitfield</b><small>sales@qlvantor.com</small><small>+1 530 555 0187</small></div></div>
      <div class="featured">
        <div class="featured-photo" role="img" aria-label="Large traditional brick house with front lawn"></div>
        <h3>Family Home, 4 Bedrooms</h3>
        <p>Spacious home on a quiet street with mature trees and a large yard.</p>
        <span class="detail-btn">View Details</span>
      </div>
    </aside>
  </div>

  <div class="container partners">
    <h2>Our <span>Partners</span></h2>
    <div class="partner-row"><i></i><i></i><i></i><i></i><i></i><i></i><i></i><i></i></div>
  </div>

  <div class="container contact-strip">
    <div><svg width="8" height="9" viewBox="0 0 8 10"><path d="M4 0a3 3 0 0 1 3 3c0 2.3-3 6.5-3 6.5S1 5.3 1 3a3 3 0 0 1 3-3z" fill="#1b95dc"/></svg>12 Orchard Road, Redding, CA</div>
    <div><svg width="8" height="8" viewBox="0 0 10 10"><path d="M2 0l2 2.5-1.2 1.2a6 6 0 0 0 3.5 3.5L7.5 6 10 8l-1.5 2C4 10 0 6 0 1.5z" fill="#1b95dc"/></svg>Phone: +1 530 555 0142</div>
    <div><svg width="8" height="8" viewBox="0 0 10 10"><rect x="1" y="2" width="8" height="6" fill="#1b95dc"/></svg>Fax: +1 530 555 0143</div>
    <div><svg width="8" height="7" viewBox="0 0 10 8"><rect width="10" height="8" fill="#1b95dc"/><path d="M0 0l5 4 5-4" stroke="#fff" fill="none"/></svg>Email: info@qlvantor.com</div>
  </div>

  <footer class="footer">
    <div class="container">
      <div><div class="brand"><span class="brand-mark"></span>QLVANTOR</div><p style="margin-top:8px">Homes, offices, farms and land across Northern California, handled by a local team you can trust.</p></div>
      <div><h4>Address</h4><ul><li>12 Orchard Road, Redding</li><li>+1 530 555 0142</li><li>info@qlvantor.com</li><li>www.qlvantor.com</li></ul></div>
      <div><h4>Links</h4><ul><li>Home</li><li>Commercial</li><li>Residential</li><li>Farm &amp; Land</li><li>Contact</li></ul></div>
      <div><h4>Newsletter</h4><p>Sign up to receive new listings and market updates each month.</p><div class="news-input"><span></span><b></b></div></div>
    </div>
  </footer>
  <div class="copyright">
    <div class="container"><span>© 2014 Qlvantor. All Rights Reserved</span><div class="socials"><i></i><i></i><i></i><i></i></div></div>
  </div>

</div>
</body>
</html>
```